International Vantor Training Company needs website redesign

Vantor 7 Global is a worldwide Vantor Training and accreditation company. We deliver water, rope, and medical training courses to emergency services, industry, government and outdoor adventure companies. We are currently looking to completely redesign our website. The main goals of this redesign are as follows:
1. Modernize the look of the website.
2. Make the website mobile compatible.
3. Focus on the international aspect of the business by making it less US focused than the current site. The new site will show us as an international brand. A separate (but similar) US site will be developed for the US market, similar in concept (but not design) to the one in place for our European office (www.vantor7europe.example).

The winning design should have:
1. Fully coded website
2. A modern, responsive design that would appeal to people in the emergency services, industrial and adventure recreation industries. Our courses are hands on, energetic, and fast paced and that should be conveyed in the design.
3. A navigation bar either at the top or side of the webpage (see attached document for page organization
4. 4 page designs: home page, template page, contact page, find a training provider page (interactive world map)

Still images and some video can be provided to aid in the design process.

Winning designer may be asked to consult on second US site.

Target Market(s)

Emergency Services (Fire, Police, Search and Rescue, Military)
Industrial Companies (Mines, Oil, Tower, etc)
Government (resource management, park rangers, road workers, etc)
Outdoor adventure companies and individuals (rafting, kayaking, highline, etc)

Industry/Entity Type

Training

Coding

Coded - Design and coding required

Number of Pages Required

4 page

Requirements
Must have
• 1. Fully coded
• 2. Mobile responsive design
• 3. Navigation bar
Nice to have
• -Dynamic images and videos
• -Interactive map or something similar so people can find a training provider in their region
Should not have
• Loud, bright, or pastel colors.

```html
<!DOCTYPE html>
<html lang="en">
<head>
<meta charset="utf-8">
<title>Vantor 7 Global – Rescue Training</title>
<link href="https://fonts.googleapis.com/css2?family=Open+Sans:wght@400;600;700&display=swap" rel="stylesheet">
<style>
:root{
  --navy:#1d3277;
  --navy-deep:#14245a;
  --red:#c4242b;
  --ink:#555a66;
  --grey-bg:#ececec;
  --footer:#1f2433;
  --footer-deep:#141824;
  --white:#ffffff;
}
*{box-sizing:border-box;margin:0;padding:0}
html,body{width:1200px;height:900px;overflow:hidden;background:var(--white);font-family:"Open Sans",Arial,sans-serif}
.page{position:absolute;left:380px;top:0;width:441px;height:895px}
.abs{position:absolute}

/* hero */
.hero{left:0;top:0;width:441px;height:180px;overflow:hidden}
.hero-photo{left:0;top:0;width:441px;height:180px;background:linear-gradient(135deg,#5b5f63 0%,#8d3a2f 35%,#2c2c30 60%,#c58a2e 85%,#6f7880 100%)}
.hero-circle{left:0;top:0}
.brand{left:29px;top:40px;font-size:9px;font-weight:700;color:var(--navy);display:flex;align-items:center;gap:4px}
.brand-dot{width:6px;height:6px;border-radius:50%;background:var(--red)}
.main-nav{left:29px;top:79px;width:84px;list-style:none}
.main-nav li{font-size:5.5px;line-height:7px;font-weight:700;color:var(--navy);padding:2px 0 2px;border-bottom:1px solid #d7dbe6}
.main-nav li:last-child{border-bottom:none}

/* courses band */
.course-band{left:0;top:180px;width:441px;height:28px;background:var(--red)}
.course-band p{position:absolute;left:29px;top:9px;font-size:6.8px;font-weight:600;color:var(--white)}
.course-icons{left:218px;top:180px;width:223px;height:28px;background:var(--navy);display:flex;justify-content:space-around;align-items:center;padding:0 8px}

/* about */
.philosophy{left:30px;top:225px;width:104px;height:166px;background:var(--navy);border:2px solid #aeb6cf}
.philosophy h3{font-size:7.5px;font-weight:600;color:var(--white);padding:5px 6px 3px;border-bottom:1px solid #6a78a8;margin:0 2px}
.philosophy p{font-size:4.6px;line-height:1.6;color:#e4e8f3;padding:5px 6px 0}
.world-map{left:6px;top:110px;width:90px;height:44px;background:radial-gradient(ellipse at center,#8e9bc4 0%,#3b4f8f 75%);border-radius:4px}
.about-title{left:147px;top:222px;font-size:8px;font-weight:600;color:var(--navy)}
.about-lead{left:147px;top:235px;width:116px;font-size:4.6px;line-height:1.75;color:var(--ink)}
.about-photo{left:270px;top:224px;width:142px;height:91px;background:linear-gradient(160deg,#7f9185 0%,#3d4a48 45%,#c4482d 70%,#2a2f33 100%)}
.about-more{left:147px;top:324px;width:265px;font-size:4.6px;line-height:1.65;color:var(--ink)}

/* what we do */
.what-we-do{left:0;top:408px;width:441px;height:163px;background:var(--grey-bg);border-top:3px solid #dcdcdc}
.what-we-do h2{position:absolute;left:30px;top:8px;font-size:10.5px;font-weight:600;color:var(--navy)}
.tabs{left:30px;top:30px;display:flex}
.tab{font-size:6.2px;line-height:10px;color:var(--red);padding:5px 6px;border:1px solid #b9b9b9;border-bottom:none;background:#d2d2d2;height:20px}
.tab.active{background:var(--white);padding:5px 12px}
.tab-panel{left:30px;top:50px;width:382px;height:96px;background:var(--white);border:1px solid #c9a7a9}
.program{position:absolute;top:8px;width:108px}
.program-img{width:108px;height:62px}
.program span{display:block;font-size:6px;color:var(--red);margin-top:5px}
.arrow{position:absolute;top:34px}

/* map */
.finder-map{left:0;top:571px;width:441px;height:135px;background:linear-gradient(120deg,#b9d1de 0%,#d8e3c6 30%,#e9e5d2 55%,#cfdcbc 80%,#b8cfd9 100%)}
.finder{left:165px;top:611px;width:115px;height:55px;background:var(--white);padding:5px 6px;box-shadow:0 1px 3px rgba(0,0,0,.2)}
.finder h4{font-size:6px;font-weight:600;color:#222}
.finder .row{font-size:4.6px;color:#333;margin-top:4px;display:flex;align-items:center;gap:3px}
.finder .radio{width:4px;height:4px;border-radius:50%;border:0.6px solid #666;display:inline-block}
.finder .radio.on{background:#555}
.finder .field{width:74px;height:10px;border:1px solid #999;margin-left:3px}
.finder .btn{position:absolute;right:7px;bottom:6px;width:42px;height:9px;background:#8f97c2;color:var(--white);font-size:4.6px;text-align:center;line-height:9px}
.pin{left:179px;top:666px}

/* feature tiles */
.tile{top:716px;width:122px;height:75px;background:linear-gradient(135deg,#0b1022 0%,#162a63 100%);color:var(--white)}
.tile svg{position:absolute;left:8px;top:17px}
.tile h5{position:absolute;right:6px;top:14px;font-size:7.8px;font-weight:600;white-space:nowrap}
.tile p{position:absolute;right:6px;top:27px;width:70px;font-size:4.2px;line-height:1.4;text-align:right;color:#dfe3ef}
.tile a{position:absolute;right:6px;top:56px;font-size:4.2px;line-height:6px;color:#e0343b;text-decoration:none;white-space:nowrap}

/* footer */
.site-footer{left:0;top:804px;width:441px;height:77px;background:var(--footer)}
.foot-col{position:absolute;top:12px}
.foot-col h6{font-size:6px;font-weight:600;color:var(--white);margin-bottom:6px}
.foot-col li{list-style:none;font-size:4.6px;line-height:1.75;color:#c4c8d3;white-space:nowrap}
.copyright{left:0;top:881px;width:441px;height:14px;background:var(--footer-deep);font-size:4.4px;color:#7c8191;text-align:center;line-height:14px}
</style>
</head>
<body>
<div class="page">

  <header class="hero abs">
    <div class="hero-photo abs" role="img" aria-label="Photo of firefighters and paramedics treating a casualty at a rescue scene"></div>
    <svg class="hero-circle abs" width="160" height="180" viewBox="0 0 160 180">
      <circle cx="-12" cy="40" r="150" fill="#ffffff" stroke="#1d3277" stroke-width="5"/>
    </svg>
    <div class="brand abs"><span class="brand-dot"></span>Vantor 7 Global</div>
    <ul class="main-nav abs">
      <li>Home</li><li>Template</li><li>Contact</li><li>Find A Training Provider</li>
    </ul>
  </header>

  <section class="course-band abs"><p>Vantor 7 Global Provides Various Types Of Courses:</p></section>
  <div class="course-icons abs">
    <svg width="16" height="22" viewBox="0 0 16 22"><path d="M8 1 C8 6 2 10 2 14 A6 6 0 0 0 14 14 C14 10 8 6 8 1Z" fill="#fff"/><path d="M1 20 Q4 18 8 20 T15 20" stroke="#fff" fill="none" stroke-width="1.2"/></svg>
    <svg width="12" height="24" viewBox="0 0 12 24"><circle cx="6" cy="3" r="2.5" fill="#fff"/><rect x="4" y="7" width="4" height="9" rx="2" fill="#fff"/><path d="M6 16 V23" stroke="#fff" stroke-width="1.5"/></svg>
    <svg width="26" height="14" viewBox="0 0 26 14"><circle cx="20" cy="4" r="2.5" fill="#fff"/><path d="M2 7 L16 5 L18 8 Z" fill="#fff"/><path d="M1 12 Q5 9 9 12 T17 12 T25 12" stroke="#fff" fill="none" stroke-width="1.3"/></svg>
    <svg width="16" height="22" viewBox="0 0 16 22"><circle cx="8" cy="3" r="2.5" fill="#fff"/><path d="M8 6 L6 13 L3 21 M7 10 L12 14 M6 13 L10 21 M7 8 L2 11" stroke="#fff" stroke-width="2" fill="none" stroke-linecap="round"/></svg>
  </div>

  <aside class="philosophy abs">
    <h3>Our Philosophy</h3>
    <p>Lorem Ipsum is simply dummy text of the printing and typesetting industry. Lorem Ipsum has been the industry's standard dummy text ever since the 1500s, when an unknown printer took a galley of type and scrambled it to make a type specimen book. It has survived not only five centuries, but also the leap into electronic typesetting, remaining essentially unchanged.</p>
    <div class="world-map abs" role="img" aria-label="World map silhouette"></div>
  </aside>

  <h2 class="about-title abs">About Vantor 7 Global</h2>
  <p class="about-lead abs">It is a long established fact that a reader will be distracted by the readable content of a page when looking at its layout. The point of using Lorem Ipsum is that it has a more-or-less normal distribution of letters, as opposed to using 'Content here, content here', making it look like readable English. Many desktop publishing packages and web page editors now use Lorem Ipsum as their default model text, and a search for 'lorem ipsum' will uncover many web sites still in their infancy.</p>
  <div class="about-photo abs" role="img" aria-label="Photo of rescue trainees in helmets on an inflatable boat"></div>
  <p class="about-more abs">There are many variations of passages of Lorem Ipsum available, but the majority have suffered alteration in some form, by injected humour, or randomised words which don't look even slightly believable. If you are going to use a passage of Lorem Ipsum, you need to be sure there isn't anything embarrassing hidden in the middle of text. All the Lorem Ipsum generators on the Internet tend to repeat predefined chunks as necessary, making this the first true generator on the Internet. It uses a dictionary of over 200 Latin words, combined with a handful of model sentence structures, to generate Lorem Ipsum which looks reasonable. The generated Lorem Ipsum is therefore always free from repetition, injected humour, or non-characteristic words etc.</p>

  <section class="what-we-do abs">
    <h2>What We Do?</h2>
    <div class="tabs abs">
      <div class="tab active">Our Programs By Industry</div>
      <div class="tab">Our Programs By Course Type</div>
      <div class="tab">Special Programs</div>
    </div>
    <div class="tab-panel abs">
      <svg class="arrow" style="left:3px" width="6" height="12" viewBox="0 0 6 12"><path d="M5 1 L1 6 L5 11" stroke="#d59a9d" fill="none"/></svg>
      <div class="program" style="left:12px"><div class="program-img" role="img" aria-label="Photo of emergency responders in a river" style="background:linear-gradient(160deg,#556a5c,#2e3b3f 60%,#b8a23a)"></div><span>Emergency Responders</span></div>
      <div class="program" style="left:136px"><div class="program-img" role="img" aria-label="Photo of industrial rope rescue team" style="background:linear-gradient(160deg,#7a2424,#c23a33 45%,#5b6e4a)"></div><span>Industry &amp; Government</span></div>
      <div class="program" style="left:260px"><div class="program-img" role="img" aria-label="Photo of a swimmer in whitewater" style="background:linear-gradient(160deg,#a37a5c,#c3502d 50%,#d9d2c4)"></div><span>Outdoor Adventure &amp; Recreation</span></div>
      <svg class="arrow" style="right:3px" width="6" height="12" viewBox="0 0 6 12"><path d="M1 1 L5 6 L1 11" stroke="#d59a9d" fill="none"/></svg>
    </div>
  </section>

  <div class="finder-map abs" role="img" aria-label="Map of Europe and Asia showing training provider locations"></div>
  <form class="finder abs">
    <h4>Find A Training Provider Near You</h4>
    <div class="row">Directions: <span class="radio on"></span> From Here <span class="radio"></span> To There</div>
    <div class="row">Address: <span class="field"></span></div>
    <div class="btn">Get Direction</div>
  </form>
  <svg class="pin abs" width="12" height="17" viewBox="0 0 12 17"><path d="M6 16 C6 16 1 9 1 6 A5 5 0 0 1 11 6 C11 9 6 16 6 16Z" fill="#c4242b"/><circle cx="6" cy="6" r="2" fill="#fff"/></svg>

  <div class="tile abs" style="left:30px">
    <svg width="40" height="40" viewBox="0 0 40 40"><rect x="4" y="7" width="32" height="29" rx="4" fill="#fff"/><rect x="11" y="3" width="3" height="8" rx="1.5" fill="#fff"/><rect x="26" y="3" width="3" height="8" rx="1.5" fill="#fff"/><g fill="#0d1430"><rect x="8" y="15" width="6" height="5"/><rect x="17" y="15" width="6" height="5"/><rect x="26" y="15" width="6" height="5"/><rect x="8" y="24" width="6" height="5"/><rect x="17" y="24" width="6" height="5"/><rect x="26" y="24" width="6" height="5"/></g></svg>
    <h5>Course Calender</h5>
    <p>There are many variations of passages of Lorem Ipsum available, but the majority have suffered alteration in some form.</p>
    <a>Search Course Calender &gt;&gt;</a>
  </div>
  <div class="tile abs" style="left:160px">
    <svg width="40" height="40" viewBox="0 0 40 40"><rect x="6" y="6" width="24" height="31" fill="none" stroke="#fff" stroke-width="2.5"/><g stroke="#fff" stroke-width="2"><path d="M10 14 H24 M10 19 H24 M10 24 H20 M10 29 H18"/></g><path d="M27 30 L36 10 L39 12 L30 32 Z" fill="#fff"/></svg>
    <h5>Course Information</h5>
    <p>There are many variations of passages of Lorem Ipsum available, but the majority have suffered alteration in some form.</p>
    <a>Read More &gt;&gt;</a>
  </div>
  <div class="tile abs" style="left:290px">
    <svg width="40" height="40" viewBox="0 0 40 40"><circle cx="20" cy="25" r="13" fill="none" stroke="#fff" stroke-width="2.5"/><path d="M7 25 H33 M20 12 V38" stroke="#fff" stroke-width="2"/><path d="M20 3 L38 10 L20 17 L2 10 Z" fill="#fff"/></svg>
    <h5>Online Learning</h5>
    <p>There are many variations of passages of Lorem Ipsum available, but the majority have suffered alteration in some form.</p>
    <a>Read More &gt;&gt;</a>
  </div>

  <footer class="site-footer abs">
    <div class="foot-col" style="left:29px"><h6>Vantor Training</h6><ul><li>Training Courses</li><li>Training Providers</li><li>Instructor Training</li><li>Course Calender</li><li>Check Vantor 7 Qualifications</li></ul></div>
    <div class="foot-col" style="left:107px"><h6>Resources</h6><ul><li>Student Downloads</li><li>Online Shop</li><li>Buy The Field Guide</li><li>Vantor Feldhandbuch</li></ul></div>
    <div class="foot-col" style="left:183px"><h6>Information</h6><ul><li>About Vantor 7 Europe</li><li>Feedback Form</li><li>Community Page</li><li>Conference 2015</li></ul></div>
    <div class="foot-col" style="left:248px"><h6>Vantor 7 Europe Ltd</h6><ul><li>A Limited Company registered in England</li><li>and Wales number 0000000</li><li>VAT registration number 000 0000 00</li><li>© 2015 Vantor 7 Europe Ltd</li></ul></div>
    <div class="foot-col" style="left:352px"><h6>Contact Us</h6><ul><li>The Old Mill</li><li>Harbour Lane</li><li>Brynmere BM4 2QT</li><li>United Kingdom</li><li>T: +44 (0) 1632 960214</li><li>E: info@vantor7europe.example</li></ul></div>
  </footer>
  <div class="copyright abs">Copyright vantor7global. All rights reserved.</div>

</div>
</body>
</html>
```